Dorsey K. Wendell Business Card

We need a business card for our company Dorsey K. Wendell Heating & Plumbing to be distributed to potential customers. It should follow the color scheme of our logo and have a modern upscale and masculine look.

The logo is attached and the info below should also be included:

5187 W. Cedar Brook Rd.
Manheim, PA 17545

Russell T. Wendell
(717) 592-0817
russelltwendell@fernmail.net
dorseykwendell.net
PA #093148

Industry/Entity Type

Business

Contact Information for Business Card

5187 W. Cedar Brook Rd.
Manheim, PA 17545

Russell T. Wendell
(717) 592-0817
russelltwendell@fernmail.net
dorseykwendell.net
PA #093148

Colors

Designer to choose colors to be used in the design.

Requirements
Must have
• Information above included

```html
<!DOCTYPE html>
<html lang="en">
<head>
<meta charset="utf-8">
<title>Dorsey K. Wendell Business Card</title>
<link rel="stylesheet" href="https://fonts.googleapis.com/css2?family=Arimo:wght@400;700&display=swap">
<style>
  :root {
    --brand-blue: #1a4fa0;
    --brand-blue-bright: #1f5bb8;
    --back-blue-light: #3a79d2;
    --back-blue-dark: #1f57b3;
    --brand-green: #8dc63f;
    --card-white: #ffffff;
    --watermark: rgba(255, 255, 255, 0.07);
    --stage: #2b2b2b;
  }
  * { margin: 0; padding: 0; box-sizing: border-box; }
  html, body { width: 900px; height: 1200px; overflow: hidden; }
  body {
    background: var(--stage);
    font-family: "Arimo", Arial, sans-serif;
    position: relative;
  }
  .card {
    position: absolute;
    left: 85px;
    width: 733px;
    height: 428px;
    border-radius: 22px;
    overflow: hidden;
  }
  .card--front { top: 138px; background: var(--card-white); }
  .card--back {
    top: 634px;
    background: linear-gradient(135deg, var(--back-blue-light) 0%, var(--back-blue-dark) 100%);
  }

  .holder { position: absolute; left: 52px; top: 56px; }
  .holder__name { font-size: 24px; font-weight: 700; color: var(--brand-blue); line-height: 1.2; }
  .holder__title { font-size: 17px; color: var(--brand-green); margin-top: 4px; }

  .brand {
    position: absolute;
    display: flex;
    align-items: center;
    gap: 12px;
    font-weight: 700;
    line-height: 1.05;
    white-space: nowrap;
  }
  .brand__square { flex: none; }
  .brand__name { text-transform: uppercase; }
  .brand--front { right: 46px; top: 58px; color: var(--brand-blue); }
  .brand--front .brand__square { width: 62px; height: 62px; background: var(--brand-blue); }
  .brand--front .brand__name { font-size: 22px; }
  .brand--back { left: 55px; top: 285px; color: var(--card-white); }
  .brand--back .brand__square { width: 82px; height: 82px; background: var(--card-white); }
  .brand--back .brand__name { font-size: 30px; }

  .watermark { position: absolute; inset: 0; }
  .watermark__item {
    position: absolute;
    display: flex;
    align-items: center;
    gap: 18px;
    color: var(--watermark);
    font-weight: 700;
    font-size: 44px;
    line-height: 1.05;
    text-transform: uppercase;
    white-space: nowrap;
  }
  .watermark__square { width: 130px; height: 130px; background: var(--watermark); flex: none; }

  .divider {
    position: absolute; left: 52px; right: 46px; top: 276px;
    height: 1px; background: var(--brand-green);
  }

  .contact { position: absolute; left: 53px; top: 294px; list-style: none; }
  .contact__item {
    display: flex; align-items: center; gap: 13px;
    font-size: 17px; color: var(--brand-blue); height: 26px;
  }
  .contact__icon { width: 19px; height: 19px; flex: none; }

  .address {
    position: absolute; right: 46px; top: 293px;
    text-align: right; font-size: 17px; line-height: 24px; color: var(--brand-blue);
    font-style: normal;
  }

  .bands { position: absolute; left: 0; bottom: 0; width: 733px; height: 32px; }
</style>
</head>
<body>

<section class="card card--front" aria-label="Business card front">
  <div class="holder">
    <div class="holder__name">Russell T. Wendell</div>
    <div class="holder__title">Managing Director</div>
  </div>

  <div class="brand brand--front">
    <span class="brand__square"></span>
    <span class="brand__name">Dorsey K. Wendell<br>Heating &amp; Plumbing</span>
  </div>

  <div class="divider"></div>

  <ul class="contact">
    <li class="contact__item">
      <svg class="contact__icon" viewBox="0 0 19 19" aria-hidden="true">
        <rect width="19" height="19" fill="var(--brand-green)"/>
        <path d="M5 4.5l2.3-.5 1.2 2.8-1.4 1.1a7 7 0 0 0 3.5 3.5l1.1-1.4 2.8 1.2-.5 2.3c-5 .3-9.3-4-9-9z" fill="#fff"/>
      </svg>
      (717) 592-0817
    </li>
    <li class="contact__item">
      <svg class="contact__icon" viewBox="0 0 19 19" aria-hidden="true">
        <rect width="19" height="19" fill="var(--brand-green)"/>
        <rect x="4" y="5.5" width="11" height="8" fill="none" stroke="#fff" stroke-width="1.2"/>
        <path d="M4 5.5l5.5 4.5 5.5-4.5" fill="none" stroke="#fff" stroke-width="1.2"/>
      </svg>
      russelltwendell@fernmail.net
    </li>
    <li class="contact__item">
      <svg class="contact__icon" viewBox="0 0 19 19" aria-hidden="true">
        <rect width="19" height="19" fill="var(--brand-green)"/>
        <circle cx="9.5" cy="9.5" r="5.5" fill="none" stroke="#fff" stroke-width="1.2"/>
        <ellipse cx="9.5" cy="9.5" rx="2.3" ry="5.5" fill="none" stroke="#fff" stroke-width="1"/>
        <path d="M4 9.5h11" stroke="#fff" stroke-width="1"/>
      </svg>
      dorseykwendell.net
    </li>
  </ul>

  <address class="address">
    5187 W. Cedar Brook Rd.<br>
    Manheim, PA 17545<br>
    PA #093148
  </address>

  <svg class="bands" viewBox="0 0 733 32" aria-hidden="true">
    <polygon points="0,13 366,13 362,22 0,22" fill="var(--brand-green)"/>
    <polygon points="371,2 733,2 733,12 367,12" fill="var(--brand-blue-bright)"/>
  </svg>
</section>

<section class="card card--back" aria-label="Business card back">
  <div class="watermark" aria-hidden="true">
    <div class="watermark__item" style="left:-180px; top:10px;">
      <span class="brand__name">Dorsey K. Wendell<br>Heating &amp; Plumbing</span>
    </div>
    <div class="watermark__item" style="left:388px; top:4px;">
      <span class="watermark__square"></span>
      <span class="brand__name">Dorsey K. Wendell<br>Heating &amp; Plumbing</span>
    </div>
    <div class="watermark__item" style="left:20px; top:150px;">
      <span class="watermark__square"></span>
      <span class="brand__name">Dorsey K. Wendell<br>Heating &amp; Plumbing</span>
    </div>
    <div class="watermark__item" style="left:645px; top:150px;">
      <span class="watermark__square"></span>
    </div>
    <div class="watermark__item" style="left:442px; top:292px;">
      <span class="watermark__square"></span>
      <span class="brand__name">Dorsey K. Wendell<br>Heating &amp; Plumbing</span>
    </div>
  </div>

  <div class="brand brand--back">
    <span class="brand__square"></span>
    <span class="brand__name">Dorsey K. Wendell<br>Heating &amp; Plumbing</span>
  </div>
</section>

</body>
</html>
```